MODERN + COOL Business Card Needed!

SUMMARY
This is for a 40+ year old family business that is transitioning to the 2nd generation and is in real need of a more modern facelift. Ive attached a company logo (I made quickly as an idea with my limited PSD skills) to start off with that you are welcome to change and draw ideas from. Ive also attached some screen shots of cards I like to give you an idea of my preferences.

WHAT WE DO
The company name is Tall Pine HK Ltd. But I prefer to just call it Tall Pine or Tall Pine with Hong Kong as kind of a sub heading on the business card. We own a factory as well as help our customers find factories to make their product. Product I mean, toys 99.9% of the time. Simple old school toys like board games, puzzles, wooden toys, baby/infant toys.

You can say we are a "sourcing" or "trading" or "consulting" company with a factory to help you do it. But since we deal with toys, i like to keep it modern and cool and fun, not serious like managing hedge funds.

WHAT WE ARE LOOKING FOR
A cool, unique looking business card that stands out. In terms of design, something modern and professional. I like darker colored cards and I like colors such as blue/green/dark gray, but am open to other colored themes. I Like bright lime green with gray, always though thats a nice combo. I prefer cards that are all colored and not so much white showing (I think). Ive attached a few screenshots of cards so take a look to get a feel of what I like.

We do alot of wooden stacking games in variety of colors too like Tovra, Lumo, Towerplix (google these to check them out). So designs that sort of resemble stacking or building would be cool but totally not necessary.

In terms of the physical aspects of the card, Im looking for a card a bit different than the standard rectangular shape. Double sided. Little things like having corner(s) be round or different angle instead of square edge I always thought was nice. Its got to be mostly a normal card size, no folding or smaller cards that fit weird in your wallet. No vertical designs. Am open to VERY different/creative shapes (as long as it still fits in a wallet good like a normal buisness card.
Updates

Hi everyone!

Just wanted to write a message to everyone to let them know all submissions are being reviewed or have been reviewed.  If I have not responded with feedback, rest assure your submission was definitely looked at in detail but I either have just been too busy to respond (alot of submissions!), or its on my to be considered list.

I respect and really enjoy receiving everyones creativity and work so I dont want it to go unrecognized - thus this message!  Feel free to submit more ideas if you like until this project ends.  Sometimes some designs just dont click but sometimes they can so you never know!

Thanks again for everyones participation and great work!

~Dev Orr

Target Market(s)

The cards are mainly handed to toy company sourcers and buyers. People I talk to ... say Pelvane for example... might want to make their next edition of Farthingale game with a reputable factory at a good cost so they can sell it to stores at a profit.

So these are the types of people I often try to talk and introduce myself and my company to.

Industry/Entity Type

Building

Colors
acd036
0392cd
00a88e
474747
606060

Requirements
Must have
• Just double sided, not plain rectangle corners, and just cool to look at and catches your eye!

Oh and the obvious business card stuff like place for name, address, number, email, etc.
Nice to have
• Think more modern and fun, not serious and old fashion (thats what we used to be!). Can use the logo I attached and you can definitely alter and change the logo or make a whole new one!

Oh and can definitely use a creative slogan if you like to think of one based on what I described in what we do.
Should not have
• Dont use fonts or text placement that might make "Tall Pine" look like "Tal Lpine"... We arent selling news papers!!

Please nothing related to education since we have the word Pine in the title, thats not our business at all.

Logo and design should not be too heavy on things related to toys, as though thats what we primarily focus on now, what we do may change over time.

```html
<!DOCTYPE html>
<html lang="en">
<head>
<meta charset="utf-8">
<title>Tall Pine Ltd — Business Card</title>
<link href="https://fonts.googleapis.com/css2?family=Quicksand:wght@600;700&family=Roboto+Condensed:wght@500&display=swap" rel="stylesheet">
<style>
  :root {
    --lime: #8dc63f;
    --lime-bright: #c8e03a;
    --yellow: #f2f06a;
    --yellow-text: #e9ea4a;
    --panel: #231f1e;
    --swoosh: #474747;
    --grey-text: #c9c9c9;
    --edge: #111;
  }
  html, body { margin: 0; padding: 0; background: #fff; overflow: hidden; }
  .canvas { position: relative; width: 736px; height: 1200px; overflow: hidden; }
  .card { position: absolute; }
  .card svg.card-shape { position: absolute; left: 0; top: 0; }
  .front { left: 0; top: 0; width: 730px; height: 444px; }
  .back { left: 8px; top: 755px; width: 724px; height: 444px; }
  .text { position: absolute; font-family: "Quicksand", sans-serif; font-weight: 700; white-space: nowrap; margin: 0; }
  .brand-mark { left: 92px; top: 112px; font-size: 28px; color: var(--yellow-text); }
  .company { left: 256px; top: 92px; font-size: 50px; color: var(--yellow-text); line-height: 1; }
  .region { left: 356px; top: 158px; font-size: 32px; color: var(--yellow-text); line-height: 1; }
  .contact { left: 64px; top: 226px; font-family: "Roboto Condensed", "Arial Narrow", sans-serif; font-weight: 500; font-size: 23px; color: var(--grey-text); letter-spacing: 1px; line-height: 30px; }
  .phone { left: 498px; top: 224px; font-size: 25px; color: var(--yellow-text); letter-spacing: 0.5px; line-height: 32px; }
  .phone-icon { position: absolute; left: 468px; top: 222px; }
  .address-label { left: 82px; top: 284px; font-size: 21px; color: var(--lime); }
  .address { left: 207px; top: 284px; font-size: 21px; color: var(--yellow-text); line-height: 31px; }
  .email { left: 466px; top: 384px; font-family: Arial, sans-serif; font-weight: 400; font-size: 16px; line-height: 18px; color: var(--lime); transform: rotate(-30deg); transform-origin: left bottom; }
  .back .back-mark { left: 86px; top: 192px; font-size: 24px; color: var(--yellow-text); }
  .tagline { left: 232px; top: 187px; font-size: 31px; color: var(--yellow-text); }
</style>
</head>
<body>
<div class="canvas">

  <section class="card front">
    <svg class="card-shape" width="730" height="444" viewBox="0 0 730 444">
      <defs>
        <linearGradient id="frameFront" x1="0" y1="0" x2="0" y2="1">
          <stop offset="0" stop-color="#8dc63f"/>
          <stop offset="1" stop-color="#fbf46e"/>
        </linearGradient>
        <radialGradient id="glow" cx="0.5" cy="0.5" r="0.5">
          <stop offset="0" stop-color="#f4ee1c"/>
          <stop offset="0.45" stop-color="#a9a418" stop-opacity="0.8"/>
          <stop offset="1" stop-color="#231f1e" stop-opacity="0"/>
        </radialGradient>
        <linearGradient id="swooshFront" x1="0" y1="0" x2="1" y2="1">
          <stop offset="0" stop-color="#4a4a48"/>
          <stop offset="1" stop-color="#2c2a29"/>
        </linearGradient>
        <linearGradient id="limeArc" x1="0" y1="0" x2="1" y2="0">
          <stop offset="0" stop-color="#8dc63f"/>
          <stop offset="1" stop-color="#e6ee5a"/>
        </linearGradient>
        <clipPath id="panelFront"><rect x="20" y="20" width="688" height="400" rx="36"/></clipPath>
      </defs>
      <rect x="1.5" y="1.5" width="726" height="440" rx="46" fill="url(#frameFront)" stroke="#111" stroke-width="3"/>
      <rect x="20" y="20" width="688" height="400" rx="36" fill="#231f1e" stroke="#8dc63f" stroke-width="3"/>
      <g clip-path="url(#panelFront)">
        <circle cx="140" cy="132" r="90" fill="url(#glow)"/>
        <path d="M442 420 C470 330 560 270 710 255 L710 420 Z" fill="url(#swooshFront)"/>
        <path d="M500 420 C530 350 600 318 710 310 L710 322 C610 332 548 362 522 420 Z" fill="url(#limeArc)"/>
        <path d="M522 420 C548 362 610 332 710 322 L710 420 Z" fill="#3a3837"/>
      </g>
    </svg>
    <p class="text brand-mark">Tall Pine</p>
    <h1 class="text company">Tall Pine Ltd</h1>
    <p class="text region">Hong Kong</p>
    <p class="text contact">CONTACT PERSON: AARON VELL</p>
    <svg class="phone-icon" width="24" height="36" viewBox="0 0 24 36" aria-hidden="true">
      <path d="M6 2 L11 2 L12 10 L8 12 C8 18 10 23 13 26 L17 23 L22 28 L19 34 C10 34 2 22 2 10 Z" fill="none" stroke="#8dc63f" stroke-width="3" stroke-linejoin="round"/>
    </svg>
    <p class="text phone">084517290</p>
    <p class="text address-label">ADDRESS:</p>
    <p class="text address">48 Harbour Lane<br>Wensley<br>HONG KONG</p>
    <p class="text email">e mail: aaronvell@tallpine.com</p>
  </section>

  <section class="card back">
    <svg class="card-shape" width="724" height="444" viewBox="0 0 724 444">
      <defs>
        <linearGradient id="frameBack" x1="0" y1="0" x2="0" y2="1">
          <stop offset="0" stop-color="#8dc63f"/>
          <stop offset="1" stop-color="#fbf46e"/>
        </linearGradient>
        <radialGradient id="greenGlow" cx="0.78" cy="0" r="0.55">
          <stop offset="0" stop-color="#7fbf2a"/>
          <stop offset="0.5" stop-color="#3f5a1a"/>
          <stop offset="1" stop-color="#231f1e"/>
        </radialGradient>
        <linearGradient id="swooshBack" x1="0" y1="0" x2="1" y2="1">
          <stop offset="0" stop-color="#4a4a48"/>
          <stop offset="1" stop-color="#2c2a29"/>
        </linearGradient>
        <clipPath id="panelBack"><rect x="20" y="20" width="684" height="402" rx="36"/></clipPath>
      </defs>
      <rect x="1.5" y="1.5" width="721" height="441" rx="46" fill="url(#frameBack)" stroke="#111" stroke-width="3"/>
      <rect x="20" y="20" width="684" height="402" rx="36" fill="url(#greenGlow)" stroke="#8dc63f" stroke-width="3"/>
      <g clip-path="url(#panelBack)">
        <path d="M20 258 C130 260 230 310 262 422 L20 422 Z" fill="url(#swooshBack)"/>
        <path d="M20 310 C110 310 170 330 200 422 L188 422 C160 340 100 322 20 322 Z" fill="#8dc63f"/>
        <path d="M20 322 C100 322 160 340 188 422 L20 422 Z" fill="#3a3837"/>
      </g>
      <path d="M198 207 L210 195 L222 207 L210 219 Z" fill="#e9ea4a"/>
    </svg>
    <p class="text back-mark">Tall Pine</p>
    <p class="text tagline">Trading, Sourcing, Consulting</p>
  </section>

</div>
</body>
</html>
```